Professional stationery for boutique management consulting business

I need branded business stationery for my consulting business, using our existing logo and website branding. We consult to senior executives to create deep cultural change needed for humane, people-centred workplaces. The key deliverables are: (A4 size) business letterheads, proposal cover, project folder, report template, email footer, business card, simple powerpoint template. A warm, empowering and expert tone of voice is important as it needs to bridge the gap between academia and industry. It should be clean and professional without feeling "over-branded".
I would like to see stationery designs that use my website colours and design elements (see attached file), especially the delta logo. Our fonts are Operetta and Sofia Pro.
Updates

Thanks for the designs sent so far. Just to confirm that our key deliverables for this project are: - (A4 size) business letterhead - (A4 size) proposal template - (A4 size) report template - Project folder, - Simple powerpoint template - Business card Many thanks

Target Market(s)

Senior executives and business professionals with an interest in business school thinking.

Industry/Entity Type

Management consulting and executive coaching

Font styles to use
Other font styles liked:
• Operetta and Sofia Pro

Colors
0054AA
0677BA
7BADD7
CADEEF
E8F1F8

Requirements
Must have
• Clean professional design that ties in closely to complement and extend the design elements in my website: marlowadvises.com
Nice to have
• Address and contact details I can edit in Microsoft Word, Outlook for Mac, etc
Should not have
• Excessive brand elements, fussy design and additional colours.

```html
<!DOCTYPE html>
<html lang="en">
<head>
<meta charset="utf-8">
<title>Marlow Advises – Stationery</title>
<link rel="stylesheet" href="https://fonts.googleapis.com/css2?family=Montserrat:wght@300;400;500&family=Arimo:wght@400;700&family=Mrs+Saint+Delafield&display=swap">
<style>
:root{
  --navy:#283472;
  --grey-band:#7b7b7b;
  --backdrop:#a9a9a9;
  --paper:#ffffff;
  --paper-shade:#ececec;
  --ink:#555;
  --ink-soft:#888;
  --rule:#9a9a9a;
}
*{margin:0;padding:0;box-sizing:border-box}
html,body{width:998px;height:1200px;overflow:hidden;background:var(--backdrop)}
.sheet{position:relative;width:998px;height:1200px}
.item{position:absolute;overflow:hidden;box-shadow:2px 3px 5px rgba(0,0,0,.35)}
.paper{background:linear-gradient(100deg,var(--paper-shade) 0%,var(--paper) 55%)}
.wordmark{font-family:"Montserrat",sans-serif;font-weight:300;color:var(--navy);white-space:nowrap;position:absolute;letter-spacing:.01em}
.wordmark.light{color:#fff}
.abs{position:absolute}
.band{position:absolute;left:0;right:0;bottom:0;height:6px;background:var(--grey-band)}
.band::before{content:"";position:absolute;left:0;top:0;bottom:0;width:var(--split);background:var(--navy)}
.band::after{content:"";position:absolute;top:0;bottom:0;left:var(--split);width:2px;background:#fff;transform:skewX(-40deg)}
.sans{font-family:"Arimo",sans-serif}
.mont{font-family:"Montserrat",sans-serif}

/* business card */
.card-front{left:151px;top:38px;width:337px;height:193px}
.card-front .wordmark{right:22px;top:58px;font-size:19px}
.card-person{left:19px;top:96px}
.card-person .name{font-family:"Arimo",sans-serif;font-weight:700;font-size:11px;color:var(--navy)}
.card-person .role{font-family:"Arimo",sans-serif;font-size:8.5px;color:var(--ink)}
.card-rule{left:19px;right:22px;top:124px;height:1px;background:var(--rule)}
.contact-list{list-style:none;font-family:"Arimo",sans-serif;color:var(--ink)}
.contact-list li{display:flex;align-items:center;gap:4px;white-space:nowrap}
.contact-list svg{flex:none}
.card-front .contact-list{left:19px;top:131px;font-size:8.5px;line-height:12.5px}
.card-address{right:22px;top:148px;text-align:right;font-size:8.5px;line-height:10px;color:var(--ink)}
.card-front .band{height:8px}
.card-back{left:519px;top:38px;width:337px;height:193px;background:var(--navy)}
.card-back .wordmark{left:0;right:0;text-align:center;top:106px;font-size:24px}

/* letterhead */
.letterhead{left:43px;top:264px;width:445px;height:629px}
.letterhead .wordmark{left:29px;top:58px;font-size:17px}
.lh-contact{left:336px;top:23px;font-size:6.6px;line-height:9px;color:var(--ink)}
.lh-contact .contact-list{position:static;margin-top:5px;line-height:10px}
.lh-rule{left:29px;right:29px;top:80px;height:1px;background:var(--rule)}
.lh-to{left:45px;top:140px;font-size:7.5px;letter-spacing:.12em;color:var(--ink)}
.lh-date{right:45px;top:140px;font-size:6px;color:var(--ink)}
.lh-recipient{left:45px;top:153px;font-size:5.6px;line-height:9.8px;color:var(--ink-soft)}
.lh-recipient .who{font-size:7px;color:var(--navy)}
.lh-body{left:45px;width:356px;top:225px;font-size:6.2px;line-height:7.9px;color:var(--ink-soft);text-align:justify}
.lh-body p{margin-bottom:8px}
.lh-signature{left:45px;top:437px;font-family:"Mrs Saint Delafield",cursive;font-size:20px;color:#333}
.lh-signer{left:44px;top:467px;font-size:7px;color:var(--ink)}
.lh-signer .title{font-size:5.8px;color:var(--ink-soft)}

/* folder closed */
.folder-closed{left:519px;top:264px;width:426px;height:301px;background:var(--navy)}
.folder-closed .wordmark{left:0;width:213px;text-align:center;top:160px;font-size:19px}
.insert-page{left:213px;top:0;width:213px;height:297px;background:linear-gradient(90deg,#d0d0d0 0%,#f4f4f4 45%,#fff 100%)}
.mini-head .wordmark{font-size:6.5px}
.mini-contact{font-family:"Arimo",sans-serif;font-size:2.8px;line-height:3.8px;color:var(--ink);text-align:left}
.mini-rule{height:.6px;background:var(--rule)}
.folder-closed .band{height:4px}

/* folder open */
.folder-open{left:519px;top:592px;width:426px;height:301px;background:linear-gradient(90deg,#fff 0%,#e2e2e2 49.9%,#cfcfcf 50%,#f1f1f1 60%,#fff 100%)}
.mini-letter{left:224px;top:15px;width:192px;height:200px;background:linear-gradient(100deg,#ededed,#fff 60%);box-shadow:0 0 3px rgba(0,0,0,.2)}
.mini-letter .mini-text{position:absolute;font-family:"Montserrat",sans-serif;color:var(--ink-soft)}
.mini-body{left:20px;width:154px;top:112px;font-size:2.7px;line-height:3.6px;text-align:justify}
.mini-body p{margin-bottom:3px}
.pockets{position:absolute;left:0;top:0}

/* envelopes */
.env-window{left:33px;top:933px;width:455px;height:198px}
.env-window .wordmark{left:13px;top:36px;font-size:11px}
.env-window .env-address{left:13px;top:50px;font-size:6px;line-height:7.5px;color:var(--ink)}
.env-flap{left:519px;top:933px;width:455px;height:198px;background:linear-gradient(100deg,#e6e6e6 0%,#fff 45%)}
.env-flap svg{position:absolute;left:0;top:0}
.env-flap .wordmark{left:0;right:0;text-align:center;top:32px;font-size:11px}
</style>
</head>
<body>
<main class="sheet">

  <!-- Business card, front -->
  <section class="item paper card-front" aria-label="Business card front">
    <div class="wordmark">Marlow Advises</div>
    <div class="abs card-person">
      <div class="name">Daniel Hartley</div>
      <div class="role">Manager</div>
    </div>
    <div class="abs card-rule"></div>
    <ul class="abs contact-list">
      <li><svg width="8" height="8" viewBox="0 0 10 10"><path d="M2 1l2 2-1 1.5c.6 1.2 1.3 1.9 2.5 2.5L7 6l2 2-1.5 1.5C4 9 1 6 .5 2.5z" fill="var(--navy)"/></svg>555-010-2100</li>
      <li><svg width="8" height="8" viewBox="0 0 10 10"><rect x="0" y="2" width="10" height="6.5" fill="var(--navy)"/><path d="M0 2l5 3.5L10 2" stroke="#fff" stroke-width=".9" fill="none"/></svg>hello@marlowadvises.com</li>
      <li><svg width="8" height="8" viewBox="0 0 10 10"><circle cx="5" cy="5" r="4.6" fill="var(--navy)"/><path d="M.5 5h9M5 .5c2 2.5 2 6.5 0 9M5 .5c-2 2.5-2 6.5 0 9" stroke="#fff" stroke-width=".6" fill="none"/></svg>www.marlowadvises.com</li>
    </ul>
    <div class="abs card-address sans">Your address, city<br>state, ZIP 0000</div>
    <div class="band" style="--split:235px"></div>
  </section>

  <!-- Business card, back -->
  <section class="item card-back" aria-label="Business card back">
    <div class="wordmark light">Marlow Advises</div>
  </section>

  <!-- Letterhead -->
  <section class="item paper letterhead" aria-label="Letterhead">
    <div class="wordmark">Marlow Advises</div>
    <div class="abs lh-contact sans">
      Your address, city<br>state, ZIP 0000
      <ul class="contact-list">
        <li><svg width="6" height="6" viewBox="0 0 10 10"><path d="M2 1l2 2-1 1.5c.6 1.2 1.3 1.9 2.5 2.5L7 6l2 2-1.5 1.5C4 9 1 6 .5 2.5z" fill="var(--navy)"/></svg>555-010-2100</li>
        <li><svg width="6" height="6" viewBox="0 0 10 10"><rect x="0" y="2" width="10" height="6.5" fill="var(--navy)"/><path d="M0 2l5 3.5L10 2" stroke="#fff" stroke-width=".9" fill="none"/></svg>hello@marlowadvises.com</li>
        <li><svg width="6" height="6" viewBox="0 0 10 10"><circle cx="5" cy="5" r="4.6" fill="var(--navy)"/><path d="M.5 5h9M5 .5c2 2.5 2 6.5 0 9M5 .5c-2 2.5-2 6.5 0 9" stroke="#fff" stroke-width=".6" fill="none"/></svg>www.marlowadvises.com</li>
      </ul>
    </div>
    <div class="abs lh-rule"></div>
    <div class="abs lh-to mont">TO</div>
    <div class="abs lh-date mont">Friday, 01/01/2018</div>
    <div class="abs lh-recipient mont">
      <div class="who">Carla Mendes</div>
      Human Resources<br>Brightwell Ltd.<br>42 Orchard Row, Ashford<br>AB1 2CD
    </div>
    <div class="abs lh-body mont">
      <p>Lorem ipsum dolor sit amet, consectetuer adipiscing elit, sed diam nonmmy nibh euismod tincidunt ut laoreet dolore magna aliquam erat volutpat. Ut wisi enim ad minim veniam, quis nostrud exerci tationmcorper suscipit lobortis nisl ut aliquip ex ea commodo consequat. Duis autem vel eum iriure dolor in hendrerit in vulputate velit esse molestie consequat, vel illum dolore eu feugiat nulla facilisis at vero eros et accumsan et iusto odio dignissim qui blandit praesent luptatum zzril delenit augue duis dolore te feugait nulla facilisi.</p>
      <p>Nam liber tempor cum soluta nobis eleifend option congue nihil imprdiet doming id quod mazim placerat facer possim assum. Typi non habent claritatem insitam;</p>
      <p>Est usus legentis in iis qui facit eorum claritatem.</p>
      <p>Investigationes demonstraverunt lectores legere me lius quod ii legunt saepius. Claritas est etiam processus dynamicus, qui sequitur mutationem consuetudium lectorum. Mirum est notare quam littera gothica, quam nunc putamus parum claram, anteposuerit litterarum formas humanitatis per seacula quarta decima et quinta decima. Eodem modo typi, qui nunc nobis videntur parum clari, fiant sollemnes in futurum.</p>
      <p>consectetuer adipiscing elit, sed diam nonummy nibh euismod tincidunt ut laoreet dolore magna aliquam erat volutpat. Ut wisi enim ad minim veniam, quis nostrud exerci tation ullamcorper suscipit lobortis nisl ut aliquip ex ea commodo consequat. Duis autem vel eum iriure dolor in hendrerit in vulputate velit esse molestie consequat, vel illum dolore eu feugiat nulla facilisis at vero eros et accumsan et iusto odio dignissim qui blandit praesent luptatum zzril delenit augue duis dolore te feugait nulla facilisi.</p>
      <p>Nam liber tempor cum soluta nobis eleifend option congue nihil imperdiet .</p>
    </div>
    <div class="abs lh-signature">peter lindqvist</div>
    <div class="abs lh-signer mont">Peter Lindqvist<div class="title">Managing Director</div></div>
    <div class="band" style="--split:358px"></div>
  </section>

  <!-- Project folder, closed with insert -->
  <section class="item folder-closed" aria-label="Project folder cover">
    <div class="wordmark light">Marlow Advises</div>
    <div class="abs insert-page">
      <div class="abs mini-head" style="left:13px;top:23px"><div class="wordmark" style="position:static">Marlow Advises</div></div>
      <div class="abs mini-contact" style="left:160px;top:8px">Your address, city<br>state, ZIP 0000<br>555-010-2100<br>hello@marlowadvises.com<br>www.marlowadvises.com</div>
      <div class="abs mini-rule" style="left:13px;right:14px;top:34px"></div>
    </div>
    <div class="band" style="--split:380px"></div>
  </section>

  <!-- Project folder, open -->
  <section class="item folder-open" aria-label="Project folder inside">
    <div class="abs mini-letter">
      <div class="abs mini-head" style="left:13px;top:30px"><div class="wordmark" style="position:static">Marlow Advises</div></div>
      <div class="abs mini-contact" style="left:145px;top:24px">Your address, city<br>state, ZIP 0000<br>555-010-2100<br>hello@marlowadvises.com<br>www.marlowadvises.com</div>
      <div class="abs mini-rule" style="left:13px;right:13px;top:40px"></div>
      <div class="mini-text" style="left:20px;top:75px;font-size:3.5px">TO</div>
      <div class="mini-text" style="right:20px;top:75px;font-size:2.8px">Friday, 01/01/2018</div>
      <div class="mini-text" style="left:20px;top:81px;font-size:2.8px;line-height:3.9px"><span style="color:var(--navy)">Carla Mendes</span><br>Human Resources<br>Brightwell Ltd.<br>42 Orchard Row, Ashford<br>AB1 2CD</div>
      <div class="mini-text mini-body">
        <p>Thank you for the time you gave us last week. This letter sets out how we would work together with your leadership team over the coming quarter, with clear steps and shared goals.</p>
        <p>We suggest a first workshop in early spring, followed by short review meetings each month.</p>
        <p>Please let us know a suitable date.</p>
        <p>We look forward to building a humane workplace with you and your people.</p>
      </div>
    </div>
    <svg class="pockets" width="426" height="301" viewBox="0 0 426 301" aria-hidden="true">
      <path d="M0 196H190Q198 196 199 206L213 301H0Z" fill="var(--navy)"/>
      <path d="M426 196H238Q229 196 228 206L213 301H426Z" fill="var(--navy)"/>
    </svg>
  </section>

  <!-- Window envelope -->
  <section class="item paper env-window" aria-label="Envelope front">
    <div class="wordmark">Marlow Advises</div>
    <div class="abs env-address sans">Your address, city<br>state, ZIP 0000</div>
    <div class="band" style="--split:369px"></div>
  </section>

  <!-- Envelope back with flap -->
  <section class="item env-flap" aria-label="Envelope back">
    <svg width="455" height="198" viewBox="0 0 455 198" aria-hidden="true">
      <path d="M6 0L14 38Q18 53 34 53H420Q436 53 440 38L449 0Z" fill="#fff" stroke="#d6d6d6" stroke-width="1"/>
    </svg>
    <div class="wordmark">Marlow Advises</div>
  </section>

</main>
</body>
</html>
```